The ONLY 100% Free Security System

We are a national home/auto insurance agency that will be offering home security systems. Our "pitch" is that we will show people (before signing any agreements) how much they can save on their home/auto insurance based on having a security system installed. This is often enough to completely offset the cost of the monthly monitoring fee. One side of the flyer will highlight "The ONLY 100% truly free security system". The other side will list the following bullet points: 1. $100's in FREE Premium Security Equipment 2. FREE Professional Installation 3. "and what no other company offers..." ZERO Cost Monitoring (up to a $74.95 per month value) How? Call our 24-hour message line for a 2-minute overview: (phone # needs to be editable)

The last bullet point (what no other company offers... ZERO cost monitoring) needs to stand out.

Target Market(s)

Homeowners and businesses

Industry/Entity Type

Insurance

Font styles to use
Serif
Sans Serif

Colors

Designer to choose colors to be used in the design.

Requirements
Must have
• Editable phone # - this is also a 5.5"(width) X 8.5" (length) flyer

```html
<!DOCTYPE html>
<html lang="en">
<head>
<meta charset="utf-8">
<title>The Only 100% Truly Free Security System</title>
<link rel="stylesheet" href="https://fonts.googleapis.com/css2?family=Roboto+Condensed:wght@400;700;900&family=Arimo:wght@400;700&display=swap">
<style>
  :root{
    --page:#e6e7e9;
    --royal:#0b4c9c;
    --royal-deep:#0a3f86;
    --violet:#3d3b93;
    --green:#05a651;
    --white:#ffffff;
    --ink:#333333;
    --muted:#5a5a5a;
  }
  *{margin:0;padding:0;box-sizing:border-box}
  html,body{width:1200px;height:927px;overflow:hidden;background:var(--page)}
  .flyer{position:relative;width:1200px;height:927px;background:var(--page)}

  /* Front side */
  .front{
    position:absolute;left:44px;top:38px;width:545px;height:842px;overflow:hidden;
    background:linear-gradient(180deg,var(--royal-deep) 0,var(--royal-deep) 172px,var(--royal) 172px,var(--royal) 562px,var(--royal-deep) 562px,#123a83 100%);
  }
  .front-art{
    position:absolute;right:0;top:0;width:140px;height:280px;
    background:linear-gradient(180deg,#ffffff 0%,#f2f5fa 100%);
  }
  .headline{
    font-family:"Roboto Condensed",sans-serif;font-weight:900;color:var(--white);
    line-height:1;position:absolute;left:44px;white-space:nowrap;transform-origin:left top;
  }
  .hl-the{top:63px;font-size:108px}
  .hl-only{top:178px;font-size:117px;transform:scaleX(1.04)}
  .hl-percent{top:270px;font-size:181px;letter-spacing:-2px;transform:scaleX(1.18)}
  .hl-free{top:438px;font-size:97px;transform:scaleX(1.19)}
  .hl-security{top:557px;font-size:107px;color:var(--green);transform:scaleX(1.07)}
  .hl-system{top:659px;font-size:110px;color:var(--green);transform:scaleX(1.02)}

  /* Back side */
  .back{
    position:absolute;left:607px;top:44px;width:546px;height:843px;
    background:linear-gradient(90deg,#f4f4f4 0%,#ffffff 6%,#ffffff 88%,#d9d9d9 100%);
    font-family:Arimo,sans-serif;color:var(--ink);
  }
  .brand{position:absolute;left:0;right:0;top:122px;text-align:center}
  .brand-name{display:inline-flex;align-items:center;gap:12px;font-weight:700;font-size:44px;color:var(--green);line-height:1}
  .brand-dot{width:20px;height:20px;border-radius:50%;background:var(--green)}
  .brand-tag{margin-top:10px;font-size:17px;color:var(--muted)}

  .perks{position:absolute;left:30px;top:252px;list-style:none;font-size:32px;line-height:1.22;color:var(--ink)}
  .perks li{position:relative;padding-left:22px;margin-bottom:18px}
  .perks li::before{content:"";position:absolute;left:0;top:17px;width:11px;height:11px;border-radius:50%;background:var(--violet)}
  .perks b{font-weight:700}

  .offer{
    position:absolute;left:-1px;top:388px;width:548px;height:293px;background:var(--violet);
    text-align:center;color:var(--white);font-family:"Roboto Condensed",sans-serif;font-weight:700;
  }
  .offer-line{display:block}
  .offer-line span{display:inline-block;transform:scaleX(1.16)}
  .offer-lead{margin-top:16px;font-size:31px;line-height:1.1}
  .offer-main{font-size:46px;line-height:1.1}
  .offer-value{font-size:31px;line-height:1.1}
  .offer-how{font-family:Arimo,sans-serif;font-weight:700;font-size:150px;line-height:1;color:var(--green);margin-top:-4px}

  .cta{position:absolute;left:0;right:0;top:700px;text-align:center;font-size:31px;line-height:1.16;color:var(--ink)}
  .cta strong{font-weight:700}
</style>
</head>
<body>
<main class="flyer">
  <section class="front">
    <div class="front-art" role="img" aria-label="Illustration of a businessman in green holding a briefcase under a blue umbrella"></div>
    <h1>
      <span class="headline hl-the">The</span>
      <span class="headline hl-only">ONLY</span>
      <span class="headline hl-percent">100%</span>
      <span class="headline hl-free">Truly Free</span>
      <span class="headline hl-security">SECURITY</span>
      <span class="headline hl-system">SYSTEM</span>
    </h1>
  </section>

  <section class="back">
    <div class="brand">
      <div class="brand-name"><span class="brand-dot"></span>Harborline Cover</div>
      <div class="brand-tag">Home &amp; Auto Coverage</div>
    </div>

    <ul class="perks">
      <li><b>$100's</b> in <b>FREE Premium</b><br>Security Equipment</li>
      <li><b>FREE</b> Professional <b>Installation</b></li>
    </ul>

    <div class="offer">
      <p class="offer-line offer-lead"><span>What no other company offers..."</span></p>
      <p class="offer-line offer-main"><span>ZERO Cost Monitoring</span></p>
      <p class="offer-line offer-value"><span>(up to a $74.95 per month value)</span></p>
      <p class="offer-how">How?</p>
    </div>

    <p class="cta"><strong>Call our 24-hour message line<br>for a 2-minute overview:</strong><br><span class="cta-phone" contenteditable="true">(phone # needs to be editable)</span></p>
  </section>
</main>
</body>
</html>
```